Commercial and Residential Paint Contractor needs website

We need a website for our residential painting, multi-family painting and commercial painting company. We paint interior and exterior of houses, apartments and commercial buildings. I would like an about us page, residential page, multi family page, commercial page and contact us. Need keywords added to website for seo opitimazation. I like this website https://www.glossfieldworks.com/

Target Market(s)

General Contractors and commercial property managers

Coding

Coded - Design and coding required

Number of Pages Required

5+ page

Font styles to use
Sans Serif

Requirements
Must have
• I need SEO keywords on pages

```html
<!DOCTYPE html>
<html lang="en">
<head>
<meta charset="utf-8">
<title>Hueline Painting | Residential, Multi Family &amp; Commercial Painters</title>
<link href="https://fonts.googleapis.com/css2?family=Montserrat:wght@500;600;700;800&family=Poppins:wght@300;400;500;600&display=swap" rel="stylesheet">
<style>
:root{
  --blue:#1b4b96;
  --blue-dark:#143a78;
  --red:#c9202f;
  --ink:#1d1d1f;
  --muted:#6b6b6b;
  --white:#ffffff;
  --line:#e6e6e6;
  --star:#f5b400;
  --orange:#f7a43a;
  --green:#b5e07f;
  --coral:#f45a4a;
  --cyan:#34b6e4;
  --yellow:#f5cf1c;
  --lilac:#b79ad6;
}
*{margin:0;padding:0;box-sizing:border-box}
html,body{width:1200px;height:4444px;overflow:hidden}
body{position:relative;font-family:"Poppins",sans-serif;color:var(--ink);background:var(--white)}
.abs{position:absolute}
h1,h2,h3,h4{font-family:"Montserrat",sans-serif}

/* top bar */
.topbar{left:0;top:0;width:1200px;height:81px}
.topbar .item{position:absolute;top:47px;font-size:12px;color:#555;display:flex;align-items:center;gap:10px}
.topbar .sep{position:absolute;top:44px;width:2px;height:24px;background:#333}
.quote-btn{position:absolute;left:979px;top:39px;width:221px;height:41px;background:var(--blue);color:#fff;border-radius:8px 0 0 8px;font:700 13px "Montserrat",sans-serif;display:flex;align-items:center;justify-content:center}

/* nav */
.nav{left:0;top:81px;width:1200px;height:88px;border-top:1px solid var(--line);background:#fff}
.brand{position:absolute;display:flex;align-items:center;gap:10px;font:700 24px "Montserrat",sans-serif;color:var(--blue);white-space:nowrap}
.brand .mark{width:14px;height:14px;background:var(--red)}
.nav .brand{left:56px;top:30px}
.menu{position:absolute;left:364px;top:0;display:flex;height:88px}
.menu a{display:flex;align-items:center;padding:0 17px;font-size:13px;color:#555;text-decoration:none;text-transform:uppercase}
.menu a.active{background:var(--blue);color:#fff}
.socials{position:absolute;right:24px;top:32px;display:flex;gap:17px}
.socials span{width:24px;height:24px;border-radius:50%;background:var(--red)}

/* hero */
.hero{left:0;top:169px;width:1200px;height:719px;background:linear-gradient(100deg,#f5f6f8 0%,#e9ecf0 55%,#dfe4ea 100%)}
.hero-photo{position:absolute;left:640px;top:0;width:560px;height:719px;background:linear-gradient(180deg,#e7eaee 0%,#c8d7e6 40%,#5b82b5 100%)}
.hero-card{position:absolute;left:98px;top:217px;width:505px;height:286px;border-radius:16px;background:linear-gradient(180deg,#d97d87 0%,#c9a0b3 55%,#8fa8d4 100%);padding:46px 44px}
.eyebrow{font:700 11px "Montserrat",sans-serif;color:#fff;text-transform:uppercase;letter-spacing:.3px}
.hero-card h1{margin-top:22px;width:405px;font-size:22px;line-height:29px;color:#fff;font-weight:700;text-transform:uppercase}
.pill{display:flex;position:absolute;height:54px;border-radius:27px;font-size:12px;color:#fff;box-shadow:0 3px 8px rgba(0,0,0,.18)}
.pill .a{background:var(--blue);border-radius:27px 0 0 27px;width:182px;display:flex;align-items:center;justify-content:center}
.pill .b{background:var(--red);border-radius:0 27px 27px 0;width:182px;display:flex;align-items:center;justify-content:center}
.pill .or{position:absolute;left:168px;top:13px;width:28px;height:28px;border-radius:50%;background:#fff;border:3px solid #9fb5dc;color:var(--blue);font-size:8px;display:flex;align-items:center;justify-content:center}

/* about */
.about{left:0;top:888px;width:1200px;height:672px;background:linear-gradient(135deg,#e84b2f 0%,#f4c02b 20%,#2f6fd0 40%,#28a65a 60%,#e7302e 80%,#f0a21c 100%)}
.about-text{position:absolute;left:98px;top:77px;width:505px;height:512px;background:var(--blue);padding:46px 43px;color:#fff}
.about-text h2{margin-top:22px;font-size:33px;line-height:43px;font-weight:700;text-transform:uppercase}
.about-text h2 em,.accent{font-style:normal;color:var(--red)}
.about-text p{margin-top:14px;font-size:14px;line-height:23px;text-align:justify}
.about-text .pill{border:2px solid rgba(255,255,255,.35)}
.about-text .pill .a{background:var(--blue-dark)}
.about-media{position:absolute;left:603px;top:77px;width:504px;height:512px;background:#fff}
.about-img{position:absolute;left:44px;top:43px;width:417px;height:344px;background:linear-gradient(135deg,#f3f4f6 0%,#dfe3e8 50%,#3a66b0 100%)}

/* services */
.services{left:0;top:1560px;width:1200px;height:716px}
.services .q{position:absolute}
.svc-box{position:absolute;left:98px;top:90px;width:1009px;height:539px;background:var(--red);padding:46px 43px;color:#fff}
.svc-box h2{margin-top:14px;font-size:31px;font-weight:800;text-transform:uppercase}
.svc-box h2 span{color:var(--blue)}
.svc{position:absolute;width:255px;color:#fff}
.svc .img{height:171px;background:linear-gradient(135deg,#dfe7f0,#9fb6cf)}
.svc h3{margin-top:28px;font-size:17px;font-weight:700;text-transform:uppercase}
.svc p{margin-top:8px;font-size:14px;line-height:23px}
.notch{position:absolute;left:556px;top:629px;width:0;height:0;border-left:44px solid transparent;border-right:44px solid transparent;border-top:44px solid #1d1d1f}

/* testimonials */
.testi{left:0;top:2276px;width:1200px;height:988px;background:#ebe8e6}
.people{position:absolute;left:0;top:0;width:1200px;height:405px;background:linear-gradient(180deg,#f0eeec 0%,#d7d2ce 60%,#5b5f6a 100%)}
.testi .eyebrow2{position:absolute;left:0;width:1200px;top:452px;text-align:center;font:600 11px "Montserrat",sans-serif;color:#555;text-transform:uppercase}
.testi h2{position:absolute;left:0;width:1200px;top:482px;text-align:center;font-size:33px;font-weight:700;text-transform:uppercase;color:var(--ink)}
.card{position:absolute;background:#fff;padding:22px;box-shadow:0 2px 8px rgba(0,0,0,.08)}
.card .av{width:60px;height:60px;border-radius:50%;background:linear-gradient(135deg,#c8b7a6,#6f5f52)}
.card p{margin-top:20px;font-size:13.5px;line-height:22px;color:#555}
.card .who{margin-top:20px;font:700 13px "Montserrat",sans-serif;text-transform:uppercase}
.card .role{margin-top:14px;font-size:12px;color:#777}
.card .stars{margin-top:12px;color:var(--star);font-size:12px;letter-spacing:1px}

/* contact */
.contact{left:0;top:3264px;width:1200px;height:753px;background:linear-gradient(90deg,var(--orange) 0 8%,var(--lilac) 92% 100%)}
.contact .strip{position:absolute}
.contact-info{position:absolute;left:98px;top:10px;width:505px;height:743px;background:var(--blue);color:#fff;padding:65px 70px}
.sub{font:500 14px "Montserrat",sans-serif;letter-spacing:2px;text-transform:uppercase;display:flex;align-items:center;gap:10px}
.sub::before{content:"";width:2px;height:14px;background:currentColor}
.contact h2{margin-top:10px;font-size:29px;font-weight:700;text-transform:uppercase}
.info-row{position:absolute;display:flex;align-items:center;gap:12px;font-size:12px}
.sq{width:22px;height:22px;border-radius:5px;background:var(--red)}
.map{position:absolute;width:365px;height:215px;background:linear-gradient(135deg,#eef0f2,#d5d9de);border:3px solid #fff}
.contact-form{position:absolute;left:603px;top:10px;width:504px;height:743px;background:var(--red);padding:65px 0;color:#fff}
.contact-form .sub{justify-content:center}
.contact-form h2{text-align:center;margin-top:22px}
.form{position:absolute;left:69px;top:150px;width:366px;height:407px;background:#fff;border-radius:8px;padding:20px 13px}
.field{height:62px;font-size:12px;color:#999;padding:6px 14px;border-bottom:18px solid var(--red)}
.field.msg{height:133px}
.send{height:48px;background:var(--blue);color:#fff;font:600 13px "Montserrat",sans-serif;display:flex;align-items:center;justify-content:center;text-transform:uppercase}

/* footer */
.footer{left:0;top:4017px;width:1200px;height:355px;background:linear-gradient(120deg,#d4e34a 0%,#f3913a 30%,#e94b8d 55%,#7fd0ef 80%,#f2d54c 100%);color:#fff}
.footer .brand{left:124px;top:58px;font-size:28px}
.footer .motto{position:absolute;left:121px;top:118px;font-size:13px}
.fcol{position:absolute;top:48px}
.fcol h4{font-weight:600;font-size:22px;text-transform:uppercase}
.fcol ul{list-style:none;margin-top:16px}
.fcol li{font-size:13px;margin-bottom:22px}
.fcol.svcs li{margin-bottom:17px;font-size:12px}
.fcol.ct li{margin-bottom:20px;font-size:12px;display:flex;gap:8px;align-items:center}
.ficons{display:flex;gap:12px}
.ficons span{width:22px;height:22px;border-radius:50%;background:var(--red)}
.copy{left:0;top:4372px;width:1200px;height:72px;background:#111;color:#fff;font-size:13px;display:flex;align-items:center;justify-content:center}
</style>
</head>
<body>

<header class="abs topbar">
  <div class="item" style="left:26px">
    <svg width="20" height="14" viewBox="0 0 20 14"><rect width="20" height="14" rx="2" fill="#c9202f"/><path d="M1 1l9 7 9-7" stroke="#fff" stroke-width="1.6" fill="none"/></svg>
    info@huelinepainting.com</div>
  <span class="sep" style="left:224px"></span>
  <div class="item" style="left:248px">
    <svg width="16" height="16" viewBox="0 0 16 16"><rect width="16" height="16" rx="3" fill="#c9202f"/><path d="M5 3l2 3-1 1c.8 1.6 1.6 2.4 3 3l1-1 3 2-1 2C7 12 4 9 3 4z" fill="#fff"/></svg>
    555 014 0123</div>
  <span class="sep" style="left:376px"></span>
  <div class="item" style="left:400px">
    <svg width="14" height="18" viewBox="0 0 14 18"><path d="M7 0a7 7 0 017 7c0 5-7 11-7 11S0 12 0 7a7 7 0 017-7z" fill="#c9202f"/><circle cx="7" cy="7" r="2.6" fill="#fff"/></svg>
    48 Marlow Street, New York. USA</div>
  <div class="quote-btn">GET A FREE QUOTE</div>
</header>

<nav class="abs nav">
  <div class="brand"><span class="mark"></span>Hueline Painting</div>
  <div class="menu">
    <a class="active" href="#">Home</a><a href="#">About</a><a href="#">Services &#9662;</a><a href="#">Blogs</a><a href="#">Contact</a>
  </div>
  <div class="socials"><span></span><span></span><span></span><span></span></div>
</nav>

<section class="abs hero">
  <div class="hero-photo" role="img" aria-label="Painter in overalls rolling white paint onto a wall beside a ladder"></div>
  <div class="hero-card">
    <div class="eyebrow">Welcome to Hueline Painting</div>
    <h1>Professional painters bring excellence to your home and workplace</h1>
    <div class="pill" style="left:44px;top:190px">
      <div class="a">Our Services</div><div class="b">Contact Us &rsaquo;</div><div class="or">OR</div>
    </div>
  </div>
</section>

<section class="abs about" role="img" aria-label="Colourful textured paint background">
  <div class="about-text">
    <div class="eyebrow">About us</div>
    <h2>Welcome to <em>Hueline<br>Painting</em></h2>
    <p>Lorem ipsum dolor sit amet, consectetur adipisicing elit, sed do eiusmod tempor incididunt ut labore et dolore magna aliqua. Ut enim ad minim veniam, quis nostrud exercitation ullamco laboris nisi ut aliquip ex ea commodo consequat. Duis aute irure dolor in reprehenderit in voluptate velit esse cillum dolore eu fugiat nulla pariatur. Excepteur sint occaecat cupidatat non proident, sunt in culpa qui officia deserunt mollit anim id est laborum.</p>
    <div class="pill" style="left:43px;top:416px;height:52px">
      <div class="a" style="width:165px">About Us</div><div class="b" style="width:170px">Contact Us &rsaquo;</div><div class="or" style="left:150px;top:10px">OR</div>
    </div>
  </div>
  <div class="about-media">
    <div class="about-img" role="img" aria-label="Designer choosing paint colours from swatches at a desk"></div>
  </div>
</section>

<section class="abs services">
  <div class="q" style="left:0;top:0;width:402px;height:358px;background:var(--orange)"></div>
  <div class="q" style="left:402px;top:0;width:402px;height:358px;background:var(--green)"></div>
  <div class="q" style="left:804px;top:0;width:396px;height:358px;background:var(--coral)"></div>
  <div class="q" style="left:0;top:358px;width:402px;height:358px;background:var(--cyan)"></div>
  <div class="q" style="left:402px;top:358px;width:402px;height:358px;background:var(--yellow)"></div>
  <div class="q" style="left:804px;top:358px;width:396px;height:358px;background:var(--lilac)"></div>
  <div class="svc-box">
    <div class="eyebrow">How we help you</div>
    <h2>Our <span>Services</span></h2>
  </div>
  <div class="svc" style="left:167px;top:247px">
    <div class="img" role="img" aria-label="Painter rolling paint on a house exterior"></div>
    <h3>Residential Painting</h3>
    <p>Click edit button to change this text. Lorem ipsum dolor sit amet, consectetur adipiscing elit. Ut elit tellus, luctus nec.</p>
  </div>
  <div class="svc" style="left:475px;top:247px">
    <div class="img" role="img" aria-label="Painting crew working in an empty apartment"></div>
    <h3>Multi Family Painting</h3>
    <p>Click edit button to change this text. Lorem ipsum dolor sit amet, consectetur adipiscing elit. Ut elit tellus, luctus nec.</p>
  </div>
  <div class="svc" style="left:783px;top:247px">
    <div class="img" role="img" aria-label="Worker in hard hat rolling paint in a commercial building"></div>
    <h3>Commercial Painting</h3>
    <p>Click edit button to change this text. Lorem ipsum dolor sit amet, consectetur adipiscing elit. Ut elit tellus, luctus nec.</p>
  </div>
  <div class="notch"></div>
</section>

<section class="abs testi">
  <div class="people" role="img" aria-label="Group of smiling clients holding a white banner"></div>
  <div class="eyebrow2">Our testimonials</div>
  <h2>Our <span class="accent">Happy</span> Clients</h2>
  <div class="card" style="left:115px;top:551px;width:302px;height:342px">
    <div class="av" role="img" aria-label="Client portrait"></div>
    <p>" Lorem ipsum dolor sit amet, consectetur adipisicing elit, sed do eiusmod tempor incididunt ut labore et dolore magna aliqua. Ut enim ad minim veniam. "</p>
    <div class="who">Owen Hale</div><div class="role">MANAGER NORTHBAY</div><div class="stars">&#9733;&#9733;&#9733;&#9733;&#9733;</div>
  </div>
  <div class="card" style="left:445px;top:543px;width:317px;height:342px">
    <div class="av" role="img" aria-label="Client portrait"></div>
    <p>" Lorem ipsum dolor sit amet, consectetur adipisicing elit, sed do eiusmod tempor incididunt ut labore et dolore magna aliqua. Ut enim ad minim veniam. "</p>
    <div class="who">Mara Lind</div><div class="role">CEO NORTHBAY</div><div class="stars">&#9733;&#9733;&#9733;&#9733;&#9733;</div>
  </div>
  <div class="card" style="left:790px;top:551px;width:300px;height:342px">
    <div class="av" role="img" aria-label="Client portrait"></div>
    <p>" Lorem ipsum dolor sit amet, consectetur adipisicing elit, sed do eiusmod tempor incididunt ut labore et dolore magna aliqua. Ut enim ad minim veniam. "</p>
    <div class="who">Tessa Vaughn</div><div class="role">Vaughn Family</div><div class="stars">&#9733;&#9733;&#9733;&#9733;&#9733;</div>
  </div>
</section>

<section class="abs contact">
  <div class="strip" style="left:0;top:380px;width:98px;height:373px;background:var(--cyan)"></div>
  <div class="strip" style="left:1107px;top:0;width:93px;height:380px;background:var(--coral)"></div>
  <div class="contact-info">
    <div class="sub">Get to know us</div>
    <h2>Contact Us</h2>
  </div>
  <div class="info-row" style="left:168px;top:187px;color:#fff">
    <svg width="20" height="14" viewBox="0 0 20 14"><rect width="20" height="14" rx="2" fill="#c9202f"/><path d="M1 1l9 7 9-7" stroke="#fff" stroke-width="1.6" fill="none"/></svg>
    info@huelinepainting.com</div>
  <div class="info-row" style="left:168px;top:253px;color:#fff">
    <svg width="18" height="18" viewBox="0 0 16 16"><rect width="16" height="16" rx="3" fill="#c9202f"/><path d="M5 3l2 3-1 1c.8 1.6 1.6 2.4 3 3l1-1 3 2-1 2C7 12 4 9 3 4z" fill="#fff"/></svg>
    555 014 0123</div>
  <div class="info-row" style="left:168px;top:320px;color:#fff">
    <svg width="14" height="18" viewBox="0 0 14 18"><path d="M7 0a7 7 0 017 7c0 5-7 11-7 11S0 12 0 7a7 7 0 017-7z" fill="#c9202f"/><circle cx="7" cy="7" r="2.6" fill="#fff"/></svg>
    48 Marlow Street, New York. USA</div>
  <div class="info-row" style="left:168px;top:392px;color:#fff"><span class="sq" style="width:14px;height:14px;border-radius:50%"></span>Our Social Links</div>
  <div class="info-row" style="left:168px;top:432px;gap:26px"><span class="sq"></span><span class="sq"></span><span class="sq" style="border-radius:50%"></span><span class="sq" style="border-radius:50%"></span></div>
  <div class="map" style="left:168px;top:473px" role="img" aria-label="Street map showing the office location"></div>
  <div class="contact-form">
    <div class="sub">Email us today</div>
    <h2>Get a Free Quote</h2>
    <div class="form">
      <div class="field">Name</div>
      <div class="field">Email</div>
      <div class="field">Phone</div>
      <div class="field msg">Write Message</div>
      <div class="send">Send Message</div>
    </div>
  </div>
</section>

<footer class="abs footer" role="img" aria-label="Colourful paint droplet background">
  <div class="brand"><span class="mark"></span>Hueline Painting</div>
  <div class="motto">We Make your Ideas Come Alive in Color</div>
  <div class="fcol" style="left:456px">
    <h4>Links</h4>
    <ul style="margin-left:18px"><li>Home</li><li>About</li><li>Services &#9662;</li><li>Blogs</li><li>Contact</li></ul>
  </div>
  <div class="fcol svcs" style="left:648px">
    <h4>Services</h4>
    <ul><li>Residential Painting</li><li>Industrial Painting</li><li>Commercial Painting</li><li>Multi Family Painting</li></ul>
  </div>
  <div class="fcol ct" style="left:866px">
    <h4>Contact Us</h4>
    <ul><li><span class="sq" style="width:16px;height:12px"></span>info@huelinepainting.com</li><li><span class="sq" style="width:16px;height:16px"></span>555 014 0123</li><li><span class="sq" style="width:14px;height:16px;border-radius:50%"></span>48 Marlow Street, New York. USA</li><li><span class="sq" style="width:14px;height:14px;border-radius:50%"></span>Our Social Links</li></ul>
    <div class="ficons"><span></span><span></span><span></span><span></span></div>
  </div>
</footer>
<div class="abs copy">Copyright © 2020 HUELINE PAINTING | Powered by HUELINE PAINTING</div>

</body>
</html>
```